Halvard Compute - Direct Mailer / Flyer

We are excited to announce the launch of our new company, Halvard Compute, a premier cohosting facility and data center dedicated to Cryptocurrency Miners. Our website, https://halvardcompute.example, provides detailed information about our offerings and showcases the innovative design schemes for the entire project.

Halvard Compute stands out in the industry by offering both GPU Hosting and ASIC Hosting services in our state-of-the-art facility, equipped with an impressive 17 Megawatts of available power. What sets us apart is our unique billing system based on actual metered power usage. We charge $0.08 for ASIC miners and $0.09 for GPU miners, ensuring cost-effectiveness and transparency for our clients.

Our commitment to excellence is evident in our use of cutting-edge technology, top-notch facilities, and strategic partnerships. These elements come together to deliver exceptional solutions tailored for real-world applications in the cryptocurrency space.

As part of our promotional efforts, we are developing a direct mailer/flyer to introduce Halvard Compute to a wider audience. This promotional material will also serve as a handout at events, to potential customers, and more. We welcome creative ideas and suggestions to maximize the versatility of this design and reach diverse target audiences effectively.

For a comprehensive overview of our services and to explore our design concepts, please visit https://halvardcompute.example. Halvard Compute is poised to revolutionize the mining industry, and we look forward to partnering with you for success in the digital currency era.

```html
<!DOCTYPE html>
<html lang="en">
<head>
<meta charset="utf-8">
<title>Halvard Compute – Cohosting Flyer</title>
<link href="https://fonts.googleapis.com/css2?family=Space+Grotesk:wght@400;500;600;700&family=Inter:wght@600;700;800&display=swap" rel="stylesheet">
<style>
  :root {
    --ink: #222326;
    --royal: #3A57F5;
    --sky: #99A8FF;
    --lavender: #E3E8FC;
    --lilac: #C8CEFA;
    --navy: #0C1650;
    --slate: #394370;
    --deep-blue: #2236B8;
    --card-grey: #F3F4F8;
    --card-grey-line: #E2E4EC;
    --card-tint: #EEF0FD;
    --card-tint-line: #D3D8F7;
    --card-accent: #DADEFA;
    --card-accent-line: #A9B4F5;
    --white: #FFFFFF;
  }
  * { box-sizing: border-box; margin: 0; padding: 0; }
  html, body { width: 848px; height: 1200px; overflow: hidden; background: var(--white); }
  .flyer {
    position: relative;
    width: 848px;
    height: 1200px;
    overflow: hidden;
    font-family: "Space Grotesk", sans-serif;
    color: var(--ink);
    background: var(--white);
  }
  .backdrop { position: absolute; inset: 0; width: 848px; height: 1200px; }

  .brand {
    position: absolute;
    top: 38px;
    left: 0;
    width: 848px;
    display: flex;
    justify-content: center;
    align-items: center;
    gap: 14px;
  }
  .brand-mark { width: 40px; height: 40px; background: var(--ink); border-radius: 3px; }
  .brand-name {
    font-family: "Space Grotesk", sans-serif;
    font-weight: 700;
    font-size: 46px;
    letter-spacing: -0.5px;
    color: var(--ink);
    line-height: 1;
  }

  .headline {
    position: absolute;
    left: 28px;
    top: 262px;
    font-size: 48px;
    font-weight: 600;
    line-height: 57px;
    letter-spacing: -0.3px;
  }
  .intro {
    position: absolute;
    left: 28px;
    top: 396px;
    font-size: 19px;
    line-height: 31px;
    letter-spacing: 0.3px;
  }
  .section-title {
    position: absolute;
    left: 28px;
    top: 496px;
    font-size: 46px;
    font-weight: 600;
    line-height: 58px;
  }

  .solution {
    position: absolute;
    width: 378px;
    height: 196px;
    padding: 22px 22px 0 28px;
    border: 1px solid var(--card-grey-line);
    background: var(--card-grey);
    border-radius: 2px;
  }
  .solution--tint { background: var(--card-tint); border-color: var(--card-tint-line); }
  .solution--accent { background: var(--card-accent); border-color: var(--card-accent-line); }
  .solution--gpu { left: 28px; top: 584px; }
  .solution--asic { left: 442px; top: 584px; }
  .solution--hardware { left: 28px; top: 803px; }
  .solution--consulting { left: 442px; top: 803px; }
  .solution-head {
    display: flex;
    justify-content: space-between;
    align-items: center;
    height: 40px;
  }
  .solution-title { font-size: 24px; font-weight: 600; }
  .solution-badge {
    font-family: "Inter", sans-serif;
    font-weight: 700;
    font-size: 15px;
    color: var(--royal);
    letter-spacing: -0.2px;
  }
  .solution-text {
    margin-top: 12px;
    font-size: 18px;
    line-height: 31px;
    letter-spacing: 0.2px;
  }

  .footer-tagline {
    position: absolute;
    left: 116px;
    top: 1103px;
    font-family: "Inter", sans-serif;
    font-weight: 800;
    font-size: 18px;
    line-height: 33px;
    color: var(--white);
    letter-spacing: -0.2px;
  }
  .contact {
    position: absolute;
    left: 505px;
    display: flex;
    align-items: center;
    gap: 16px;
    color: var(--white);
    font-family: "Inter", sans-serif;
    font-weight: 600;
    font-size: 17px;
    white-space: nowrap;
  }
  .contact--phone { top: 1094px; }
  .contact--mail { top: 1136px; }
  .contact-icon { width: 26px; height: 26px; flex: none; }
</style>
</head>
<body>
<main class="flyer">
  <svg class="backdrop" viewBox="0 0 1623 2296" preserveAspectRatio="none" aria-hidden="true">
    <polygon points="75,0 1623,0 1623,478 575,478" fill="var(--lavender)"/>
    <polygon points="0,0 30,0 432,395 0,396" fill="var(--royal)"/>
    <polygon points="965,350 1077,350 1190,458 1072,460" fill="var(--lilac)"/>
    <polygon points="1000,240 1623,240 1623,840" fill="var(--royal)"/>
    <polygon points="882,505 1233,498 1578,828 1220,847" fill="var(--sky)"/>
    <rect x="0" y="2012" width="1623" height="284" fill="var(--navy)"/>
    <polygon points="0,2012 555,2012 270,2296 0,2296" fill="var(--slate)"/>
    <polygon points="0,2085 228,2085 0,2296" fill="var(--royal)"/>
    <polygon points="20,2296 135,2185 250,2185 140,2296" fill="var(--deep-blue)"/>
  </svg>

  <header class="brand">
    <span class="brand-mark"></span>
    <span class="brand-name">Halvard Compute</span>
  </header>

  <h1 class="headline">Transform Mining<br>With Cohosting</h1>
  <p class="intro">Miners deserve the best - choose the<br>hosting company that delivers excellence!</p>

  <h2 class="section-title">Our Solutions</h2>

  <article class="solution solution--gpu">
    <div class="solution-head"><h3 class="solution-title">GPU Hosting</h3></div>
    <p class="solution-text">Begin your GPU Hosting journey<br>with rates starting at $0.09 kWh,<br>accepting all equipment.</p>
  </article>

  <article class="solution solution--tint solution--asic">
    <div class="solution-head"><h3 class="solution-title">ASIC Hosting</h3><span class="solution-badge">MOST POPULAR</span></div>
    <p class="solution-text">Get your ASICs directly from us or<br>send yours in today, starting at an<br>all-in rate of $0.08 kWh.</p>
  </article>

  <article class="solution solution--hardware">
    <div class="solution-head"><h3 class="solution-title">Mining Hardware</h3></div>
    <p class="solution-text">Looking for mining hardware?<br>Our equipment comes with no<br>additional markup, ever.</p>
  </article>

  <article class="solution solution--accent solution--consulting">
    <div class="solution-head"><h3 class="solution-title">Crypto Consulting</h3><span class="solution-badge">BEST VALUE</span></div>
    <p class="solution-text">Enjoy complete White Glove<br>Services for setup, insurance, and<br>tax consulting.</p>
  </article>

  <p class="footer-tagline">METERED, RELIABLE, SECURE -<br>MINERS DESERVE THE BEST HOSTING.</p>

  <div class="contact contact--phone">
    <svg class="contact-icon" viewBox="0 0 24 24" fill="none" stroke="currentColor" stroke-width="1.2" aria-hidden="true">
      <path d="M5 3l3.5 0 1.5 4.5-2.2 1.5a11 11 0 0 0 7.2 7.2l1.5-2.2 4.5 1.5 0 3.5a2 2 0 0 1-2.2 2A17 17 0 0 1 3 5.2 2 2 0 0 1 5 3z"/>
      <path d="M14 3.5a7 7 0 0 1 6.5 6.5M14 7a3.5 3.5 0 0 1 3 3"/>
    </svg>
    <span>+1 555-014-2290</span>
  </div>
  <div class="contact contact--mail">
    <svg class="contact-icon" viewBox="0 0 24 24" fill="none" stroke="currentColor" stroke-width="1.2" aria-hidden="true">
      <rect x="2" y="5" width="20" height="14"/>
      <path d="M2 5l10 8 10-8M2 19l7.5-7.5M22 19l-7.5-7.5"/>
    </svg>
    <span>hello@halvardcompute.example</span>
  </div>
</main>
</body>
</html>
```